Smartphone Social app needs an app design team

We need a smartphone app design for new company based in the NYC area called "vLoop Systems, Inc." We are a smartphone application development company focused on utilizing NearTag technologies to facilitate meeting and socializing with people that are in proximity to you.
Our first app is called vLoopmingle.net which helps people that are in physical proximity break the ice and encourages mingling with people at a party or an event.
The final design should communicate a sense of bringing social networking back to being human and meeting people in the real world.
Should be fun, contemporary, and communicate a sense of local area networking (physical world).
The scope of this design mockups that we are looking for would to design a people bingo like game for the phone facilitating meeting and breaking the ice with people in proximity with you.
When you’re ready to play, the game would provide each participant in proximity a bingo card with peoples profile characteristics and traits printed in each box. The guests have 30 minutes to mingle, introducing themselves, and find people who match the traits on the card. They must put the person’s profile picture in the corresponding box.
The first person to fill five boxes across or down yells BINGO! and that person wins the game.
Updates

Please see updated brief, describing more clearly the people bingo game concept. Thanks for your interest in designing this feature for our social app.

Reason: Changed and added more clarity to brief

Hi designers, I Updated the project brief to clarify Bingo game concept. Please add designs to simulate a bingo game concept. I know the size of the screen doesn't facilitate a bingo game, but think of way to get the same user experience with a small screen. Thanks, Owen

To all Designers, I have uploaded the new Logo for vLoopmingle and would like everyone to use the attached logos and assimilate the colors in the design. Thanks very much, Owen K.

Reason: Further clarification on app posted a few days ago.

Target Market(s)

Young adults 21-30
- College Students
- Young business professional

Industry/Entity Type

It Company

Font styles to use
Sans Serif

Requirements
Must have
• Ability to host an event
Message people in proximity to you to join the fun and download app
Build profile from GR and Trellix
See profile and compatible traits and or dislikes (like went to same school, etc.)
Develop UX for a people bingo like game to get people to mingle and learn about each other

```html
<!DOCTYPE html>
<html lang="en">
<head>
<meta charset="utf-8">
<title>vLoopmingle – App Flow</title>
<link rel="stylesheet" href="https://fonts.googleapis.com/css2?family=Mulish:wght@400;500;600&family=Source+Sans+3:wght@300;400;600;700&display=swap">
<style>
  :root {
    --bg: #eceeef;
    --orange: #e8890c;
    --orange-soft: #fbe6cc;
    --orange-pale: #fdf3e6;
    --white: #ffffff;
    --ink: #3d3d3d;
    --muted: #8a8a8a;
    --grey-card: #dedede;
    --grey-dot: #7b7b7b;
    --board: #e4e4e4;
    --social-a: #3b5a9a;
    --social-b: #4a8cc4;
    --caption: #555a5e;
    --photo-a: #8a7a66;
    --photo-b: #5e5148;
  }
  * { box-sizing: border-box; margin: 0; padding: 0; }
  html, body { width: 1200px; height: 600px; overflow: hidden; }
  body {
    background: var(--bg);
    font-family: "Source Sans 3", "Helvetica Neue", Arial, sans-serif;
    color: var(--ink);
    position: relative;
  }
  .screen {
    position: absolute;
    background: var(--white);
    overflow: hidden;
    box-shadow: 0 2px 8px rgba(0,0,0,.12);
  }
  .screen--login { left: 109px; top: 147px; width: 165px; height: 246px; background: var(--orange); }
  .screen--scan { left: 365px; top: 159px; width: 147px; height: 222px; }
  .screen--profile { left: 565px; top: 159px; width: 147px; height: 222px; }
  .screen--board { left: 765px; top: 159px; width: 147px; height: 222px; }
  .screen--feed { left: 967px; top: 159px; width: 147px; height: 222px; background: #fbfbfb; }

  .app-bar {
    height: 21px; background: var(--orange); color: var(--white);
    display: flex; align-items: center; justify-content: space-between;
    padding: 0 6px; font-size: 10px;
  }
  .app-bar svg { width: 10px; height: 10px; fill: var(--white); display: block; }
  .app-bar__title { font-size: 10.5px; }

  /* login */
  .brand { position: absolute; top: 52px; left: 0; right: 0; text-align: center; color: var(--white); }
  .brand__mark { width: 30px; height: 30px; border-radius: 50%; background: var(--white); margin: 0 auto 12px; }
  .brand__name { font-size: 19px; font-weight: 400; letter-spacing: -.2px; }
  .brand__tagline { font-size: 10px; margin-top: 8px; }
  .auth-button {
    position: absolute; left: 32px; width: 101px; height: 17px;
    display: flex; align-items: center; gap: 6px; padding-left: 3px;
    color: var(--white); font-size: 7.5px; font-weight: 600;
  }
  .auth-button--frendzibo { top: 180px; background: var(--social-a); }
  .auth-button--jobquorra { top: 205px; background: var(--social-b); }
  .auth-button__square { width: 11px; height: 11px; background: var(--white); opacity: .9; }

  /* scan */
  .radar { position: absolute; top: 33px; left: 9px; width: 130px; height: 130px; border-radius: 50%;
    background: var(--orange-pale); border: 1px solid var(--orange); }
  .radar__inner { position: absolute; top: 32px; left: 32px; width: 64px; height: 64px; border-radius: 50%;
    background: var(--orange-soft); border: 1px solid var(--orange); }
  .radar__photo { position: absolute; top: 9px; left: 9px; width: 44px; height: 44px; border-radius: 50%;
    background: linear-gradient(135deg, #6d8fa8, #3f4a55); border: 2px solid var(--orange); }
  .scan-note { position: absolute; top: 173px; width: 100%; text-align: center; font-size: 6.5px; }
  .primary-button { position: absolute; top: 188px; left: 14px; width: 119px; height: 20px; background: var(--orange);
    color: var(--white); font-size: 8px; display: flex; align-items: center; justify-content: center; gap: 5px; }
  .primary-button__dot { width: 9px; height: 9px; border-radius: 50%; border: 1px solid var(--white); }

  /* profile */
  .trait-card { position: absolute; top: 28px; left: 18px; width: 111px; height: 132px; background: var(--white);
    box-shadow: 0 0 3px rgba(0,0,0,.2); }
  .trait-card__head { height: 47px; background: var(--grey-card); display: flex; align-items: center; justify-content: center; }
  .unknown { border-radius: 50%; background: var(--grey-dot); color: var(--white); display: flex; align-items: center;
    justify-content: center; font-weight: 600; }
  .trait-card__head .unknown { width: 38px; height: 38px; border: 2px solid var(--white); font-size: 18px; }
  .trait-list { list-style: none; padding: 8px 0 0 10px; font-size: 6px; }
  .trait-list li { margin-bottom: 5px; }
  .trait-list li::before { content: "•"; margin-right: 4px; }
  .card-peek { position: absolute; top: 28px; width: 8px; height: 132px; background: var(--white); box-shadow: 0 0 3px rgba(0,0,0,.2); }
  .card-peek--left { left: -2px; } .card-peek--right { right: -2px; }
  .carousel { position: absolute; top: 166px; left: 0; right: 0; height: 56px; background: #f3f3f3;
    display: flex; align-items: center; gap: 9px; }
  .avatar { width: 40px; height: 40px; border-radius: 50%; border: 2px solid var(--orange); flex: none; }
  .avatar--a { background: linear-gradient(135deg, var(--photo-a), var(--photo-b)); }
  .avatar--first { margin-left: -18px; }
  .avatar--b { background: linear-gradient(135deg, #c9a07a, #5c6b7a); }
  .avatar--c { background: linear-gradient(135deg, #3a3430, #6f5a49); }

  /* board */
  .board { position: absolute; top: 34px; left: 9px; width: 129px; height: 133px; background: var(--board);
    display: grid; grid-template-columns: repeat(5, 22px); gap: 4px; padding: 5px 6px; align-content: start; }
  .board .unknown { width: 22px; height: 22px; font-size: 9px; border: 1px solid var(--white); }
  .board .matched { width: 22px; height: 22px; border-radius: 50%; border: 1px solid var(--white);
    background: linear-gradient(135deg, #c48c5c, #4e3f36); }
  .board .matched--ringed { border-color: var(--orange); }
  .board-count { position: absolute; top: 180px; width: 100%; text-align: center; color: var(--orange); font-size: 11px; font-weight: 700; }
  .board-caption { position: absolute; top: 195px; width: 100%; text-align: center; font-size: 6px; }

  /* feed */
  .app-bar--feed { justify-content: flex-start; gap: 50px; }
  .tabs { position: absolute; top: 24px; left: 6px; right: 6px; display: flex; }
  .tab { flex: 1; height: 13px; font-size: 6.5px; display: flex; align-items: center; justify-content: center; }
  .tab--active { background: var(--orange); color: var(--white); }
  .empty-state { position: absolute; top: 95px; width: 100%; text-align: center; }
  .empty-state__title { font-size: 9px; }
  .empty-state__text { font-size: 6px; color: var(--muted); margin: 3px auto 0; width: 100px; line-height: 1.2; }
  .camera-button { position: absolute; top: 173px; left: 57px; width: 33px; height: 33px; border-radius: 50%;
    background: var(--orange); display: flex; align-items: center; justify-content: center; }
  .camera-button svg { width: 16px; height: 16px; }

  /* captions */
  .step { position: absolute; top: 471px; width: 200px; text-align: center; color: var(--caption);
    font-family: "Mulish", "Helvetica Neue", Arial, sans-serif;
    font-size: 17px; font-weight: 500; line-height: 20.5px; letter-spacing: .2px; }
  .step--first { top: 492px; }
  .step__number { display: block; }
</style>
</head>
<body>

<svg width="0" height="0" style="position:absolute">
  <defs>
    <symbol id="icon-gear" viewBox="0 0 10 10"><circle cx="5" cy="5" r="3.2" fill="none" stroke="#fff" stroke-width="1.6" stroke-dasharray="1.6 1"/><circle cx="5" cy="5" r="1.2"/></symbol>
    <symbol id="icon-grid" viewBox="0 0 10 10"><rect x="0" y="0" width="4.4" height="4.4"/><rect x="5.6" y="0" width="4.4" height="4.4"/><rect x="0" y="5.6" width="4.4" height="4.4"/><rect x="5.6" y="5.6" width="4.4" height="4.4"/></symbol>
    <symbol id="icon-chat" viewBox="0 0 10 10"><ellipse cx="4" cy="4" rx="4" ry="3"/><ellipse cx="6.5" cy="6" rx="3.4" ry="2.6"/></symbol>
  </defs>
</svg>

<section class="screen screen--login">
  <div class="brand">
    <div class="brand__mark"></div>
    <div class="brand__name">vLoopmingle</div>
    <div class="brand__tagline">Social is human again</div>
  </div>
  <div class="auth-button auth-button--frendzibo"><span class="auth-button__square"></span>Login with Frendzibo</div>
  <div class="auth-button auth-button--jobquorra"><span class="auth-button__square"></span>Connect with Jobquorra</div>
</section>

<section class="screen screen--scan">
  <header class="app-bar">
    <svg><use href="#icon-gear"/></svg><span class="app-bar__title">vLoopmingle</span><svg><use href="#icon-grid"/></svg>
  </header>
  <div class="radar"><div class="radar__inner"><div class="radar__photo" role="img" aria-label="User profile photo"></div></div></div>
  <p class="scan-note">There are 9 people in your vicinity</p>
  <div class="primary-button"><span class="primary-button__dot"></span>Invite your friends</div>
</section>

<section class="screen screen--profile">
  <header class="app-bar">
    <svg><use href="#icon-gear"/></svg><span class="app-bar__title">vLoopmingle</span><svg><use href="#icon-grid"/></svg>
  </header>
  <div class="card-peek card-peek--left"></div>
  <div class="card-peek card-peek--right"></div>
  <article class="trait-card">
    <div class="trait-card__head"><div class="unknown">?</div></div>
    <ul class="trait-list">
      <li>Loves animals</li>
      <li>Enjoy being outdoors</li>
      <li>Very active person</li>
      <li>Energetic</li>
      <li>Loves to travel</li>
    </ul>
  </article>
  <div class="carousel">
    <div class="avatar avatar--a avatar--first" role="img" aria-label="Guest profile photo"></div>
    <div class="avatar avatar--b" role="img" aria-label="Guest profile photo"></div>
    <div class="avatar avatar--c" role="img" aria-label="Guest profile photo"></div>
    <div class="avatar avatar--a" role="img" aria-label="Guest profile photo"></div>
  </div>
</section>

<section class="screen screen--board">
  <header class="app-bar">
    <svg><use href="#icon-gear"/></svg><span class="app-bar__title">Match Board</span><svg><use href="#icon-chat"/></svg>
  </header>
  <div class="board">
    <div class="unknown">?</div><div class="unknown">?</div><div class="unknown">?</div><div class="unknown">?</div><div class="unknown">?</div>
    <div class="matched" role="img" aria-label="Matched guest photo"></div><div class="unknown">?</div><div class="matched" role="img" aria-label="Matched guest photo"></div><div class="unknown">?</div><div class="unknown">?</div>
    <div class="matched" role="img" aria-label="Matched guest photo"></div><div class="unknown">?</div><div class="matched" role="img" aria-label="Matched guest photo"></div><div class="unknown">?</div><div class="matched matched--ringed" role="img" aria-label="Matched guest photo"></div>
    <div class="unknown">?</div><div class="unknown">?</div><div class="matched" role="img" aria-label="Matched guest photo"></div><div class="unknown">?</div><div class="unknown">?</div>
    <div class="matched" role="img" aria-label="Matched guest photo"></div><div class="unknown">?</div><div class="unknown">?</div><div class="unknown">?</div><div class="matched" role="img" aria-label="Matched guest photo"></div>
  </div>
  <p class="board-count">7 of 25</p>
  <p class="board-caption">people's profiles have been matched.</p>
</section>

<section class="screen screen--feed">
  <header class="app-bar app-bar--feed">
    <svg><use href="#icon-grid"/></svg><svg><use href="#icon-chat"/></svg>
  </header>
  <nav class="tabs"><span class="tab tab--active">Feed</span><span class="tab">My Messages</span></nav>
  <div class="empty-state">
    <p class="empty-state__title">No Recent Activity</p>
    <p class="empty-state__text">Here's where you can see who likes your character</p>
  </div>
  <div class="camera-button">
    <svg viewBox="0 0 16 16"><rect x="1" y="4" width="14" height="10" rx="2" fill="#fff"/><rect x="5" y="2" width="6" height="3" rx="1" fill="#fff"/><circle cx="8" cy="9" r="3" fill="#e8890c"/><circle cx="8" cy="9" r="1.8" fill="#fff"/></svg>
  </div>
</section>

<p class="step step--first" style="left:91px"><span class="step__number">1</span>Log In or Sign Up</p>
<p class="step" style="left:337px"><span class="step__number">2</span>Geo-scan<br>your location</p>
<p class="step" style="left:538px"><span class="step__number">3</span>Match the profile<br>to the character</p>
<p class="step" style="left:739px"><span class="step__number">4</span>Match 5 profiles<br>across or down<br>and win the game</p>
<p class="step" style="left:941px"><span class="step__number">5</span>View the activities<br>and messages</p>

</body>
</html>
```